Larkspur Ridge Management - Business Cards

I need business cards. My current logo was designed by a designer at this site and I very much like and am happy with the results. I would like a business card that is trendy, unique, current yet professional. I deal with high net worth clients daily

Target Market(s)

Out of state investors looking to get into the rental market in Ohio

Industry/Entity Type

Property Management, Consulting

Contact Information for Business Card

Name, Title (Chief Financial Officer) office phone number (555) 817-3094 website address larkridgemgmt.example

Font styles to use
Sans Serif

Colors
0054AA
0677BA
7BADD7
CADEEF
E8F1F8
0094D4
00A9DD
6FCCEA
C7EBF8
E9F6FB
00AB8E
00BBA5
67D7C9
C6EFE9
E9F9F6

```html
<!DOCTYPE html>
<html lang="en">
<head>
<meta charset="utf-8">
<title>Larkspur Ridge Management – Business Cards</title>
<link href="https://fonts.googleapis.com/css2?family=Poppins:wght@400;500;700&display=swap" rel="stylesheet">
<style>
  :root {
    --navy: #0a1541;
    --navy-deep: #061036;
    --red: #d0262d;
    --ink: #1d2233;
    --rule: #c9cde0;
    --page: #ececec;
    --white: #ffffff;
  }
  * { box-sizing: border-box; margin: 0; padding: 0; }
  html, body {
    width: 891px; height: 1200px; overflow: hidden;
    background: var(--page);
    font-family: "Poppins", sans-serif;
  }
  .card {
    position: absolute; left: 78px; width: 735px; height: 420px;
    overflow: hidden;
  }
  .card--front {
    top: 110px;
    background: radial-gradient(circle at 85% 65%, #0d1a4a 0%, var(--navy-deep) 60%);
  }
  .card--back { top: 671px; background: linear-gradient(135deg, #fafbfc, #eef0f3); }

  .front__pennant { position: absolute; left: 0; top: 0; }
  .front__name {
    position: absolute; left: 218px; width: 299px; top: 112px;
    text-align: center; color: var(--navy);
    font-weight: 700; font-size: 31px; line-height: 1.15; text-transform: uppercase;
  }
  .front__urlrow {
    position: absolute; left: 0; top: 342px; width: 735px; height: 28px;
    display: flex; align-items: center; gap: 6px;
  }
  .front__rule { flex: 1; height: 1px; background: var(--rule); margin-top: 14px; }
  .front__url {
    flex: none; color: var(--white);
    font-size: 19px; letter-spacing: 2px; line-height: 28px; white-space: nowrap;
  }
  .front__url b { color: var(--red); font-weight: 700; }

  .back__panel { position: absolute; left: 0; top: 0; }
  .back__name {
    position: absolute; left: 39px; top: 114px;
    color: var(--red); font-weight: 700; font-size: 38px; line-height: 44px; letter-spacing: -0.5px;
  }
  .back__title {
    position: absolute; left: 39px; top: 155px;
    color: var(--ink); font-size: 16.5px; line-height: 20px;
  }
  .back__divider { position: absolute; left: 39px; top: 191px; width: 152px; height: 1px; background: var(--ink); }
  .back__bar { position: absolute; left: 40px; top: 222px; width: 3px; height: 79px; background: var(--red); }
  .contact { position: absolute; left: 51px; top: 222px; list-style: none; }
  .contact li {
    display: flex; align-items: center; gap: 6px; height: 27px;
    color: var(--ink); font-size: 15.5px; white-space: nowrap;
  }
  .contact svg { width: 17px; height: 17px; flex: none; }
  .back__brand {
    position: absolute; left: 520px; width: 210px; top: 160px;
    text-align: center; color: var(--white);
    font-weight: 700; font-size: 24px; line-height: 1.2; text-transform: uppercase;
  }
</style>
</head>
<body>
  <section class="card card--front">
    <svg class="front__pennant" width="735" height="420" viewBox="0 0 735 420">
      <polygon points="218,0 517,0 517,240 367,326 218,240" fill="#ffffff"/>
    </svg>
    <p class="front__name">Larkspur<br>Ridge<br>Management</p>
    <div class="front__urlrow">
      <span class="front__rule"></span>
      <p class="front__url">www.<b>larkridgemgmt</b>.example</p>
      <span class="front__rule"></span>
    </div>
  </section>

  <section class="card card--back">
    <svg class="back__panel" width="735" height="420" viewBox="0 0 735 420">
      <polygon points="590,0 735,0 735,420 590,420 524,300 524,115" fill="#0a1541"/>
    </svg>
    <h1 class="back__name">Dana Whitfield</h1>
    <p class="back__title">CHIEF FINANCIAL OFFICER</p>
    <div class="back__divider"></div>
    <div class="back__bar"></div>
    <ul class="contact">
      <li>
        <svg viewBox="0 0 20 20" aria-hidden="true"><circle cx="10" cy="10" r="10" fill="#0a1541"/><path d="M7 5.5l1.6 2.4-1 1.1a7 7 0 0 0 3.4 3.4l1.1-1 2.4 1.6-.8 1.6c-3.6.2-7.7-3.9-7.5-7.5z" fill="#fff"/></svg>
        (555) 817-3094
      </li>
      <li>
        <svg viewBox="0 0 20 20" aria-hidden="true"><circle cx="10" cy="10" r="10" fill="#0a1541"/><rect x="5" y="6.5" width="10" height="7" rx="1" fill="#fff"/><path d="M5.4 7l4.6 3.6L14.6 7" stroke="#0a1541" stroke-width="1" fill="none"/></svg>
        info@larkspurridgemgmt.example
      </li>
      <li>
        <svg viewBox="0 0 20 20" aria-hidden="true"><circle cx="10" cy="10" r="10" fill="#0a1541"/><circle cx="10" cy="10" r="5" stroke="#fff" stroke-width="1.2" fill="none"/><path d="M5 10h10M10 5c-2.4 3-2.4 7 0 10M10 5c2.4 3 2.4 7 0 10" stroke="#fff" stroke-width="1" fill="none"/></svg>
        www.larkridgemgmt.example
      </li>
    </ul>
    <p class="back__brand">Larkspur<br>Ridge<br>Management</p>
  </section>
</body>
</html>
```